Wallet/Purse themed website design

We need a simple but visually stunning graphic design for a new web based company called "pursevaultly.net".

PurseVaultly is an online/phone app offering extremely secure backup/storage for our users' personal documentation, such as credit cards, ID, passports, certificates, insurance etc.

Documents will be uploaded via a mobile app (initially zPad) to the storage. Retrieval is only possible via login together with bank level authentication (using personal questions).

Our service will not prevent the theft of our customer's physical wallet however our retrieval service can be accessed anywhere online and assist with the replacement. (for example a lost passport will require a new passport request which requires details of the lost passport number/details).
The key audiences for PurseVaultly include holidaymakers, businessmen, individuals, banking customers

We have specified that the initial design needs only to have 3 pages - home page, login page, wallet contents retrieval page.

Common themes of the following should be strongly brought to bear on the pages:
-Leather wallet/stitching
-Secure/safe/private/encryted
-Personal - for example family holiday
-Access anywhere
-Pick pockets can easily steal your wallet
Updates

Thank you for all of your submissions!  This was our first attempt to source a design via Studio Flock and we will certainly use this resource again.

Thank you.

Target Market(s)

Industry/Entity Type

Graphic Design

Requirements
Must have
• 3 pages - home page, login page, wallet contents retrieval page.
Nice to have
• Modern UI design appealing to families and individuals

```html
<!DOCTYPE html>
<html lang="en">
<head>
<meta charset="utf-8">
<title>Pursevaultly.net — Screens</title>
<link rel="stylesheet" href="https://fonts.googleapis.com/css2?family=Didact+Gothic&family=Cabin:wght@500&display=swap">
<style>
  :root {
    --sea-blue: #0250a0;
    --deep-blue: #003c82;
    --night-blue: #08294f;
    --panel-orange: #f26a22;
    --button-blue: #0152a0;
    --white: #ffffff;
  }
  * { box-sizing: border-box; margin: 0; padding: 0; }
  html, body { width: 1200px; height: 900px; overflow: hidden; }
  body { font-family: "Cabin", "Trebuchet MS", sans-serif; color: var(--white); }
  .canvas { position: relative; width: 1200px; height: 900px; background: var(--deep-blue); overflow: hidden; }
  .backdrop { position: absolute; inset: 0; }
  .site-title {
    position: absolute; left: 0; width: 1172px; top: 66px; text-align: center;
    font-family: "Didact Gothic", "Century Gothic", sans-serif; font-size: 82px; line-height: 1;
    letter-spacing: -1px; color: var(--white);
    text-shadow: 0 3px 10px rgba(180,210,255,0.55), 0 14px 10px rgba(255,255,255,0.18);
  }
  .panel {
    position: absolute; top: 157px; height: 555px; background: var(--panel-orange);
    box-shadow: 0 0 4px 2px rgba(242,106,34,0.55);
  }
  .panel--brand { left: 76px; width: 342px; }
  .panel--login { left: 436px; width: 327px; }
  .panel--home { left: 780px; width: 337px; }
  .panel-heading {
    position: absolute; top: 14px; font-size: 31px; font-weight: 500; line-height: 34px; white-space: nowrap;
  }
  .panel--brand .panel-heading { left: 18px; }
  .panel--login .panel-heading { left: 18px; }
  .panel--home .panel-heading { left: 31px; }
  .heading-icon { position: absolute; }
  .preview-box { position: absolute; left: 26px; top: 89px; width: 289px; height: 265px; background: var(--white); }
  .quick-icon { position: absolute; top: 378px; height: 52px; }
  .footer-link { position: absolute; top: 514px; font-size: 18px; }
  .field-label { position: absolute; left: 7px; font-size: 24px; line-height: 28px; }
  .field-input { position: absolute; left: 143px; width: 172px; height: 29px; background: var(--white); border: 0; }
  .action-button {
    position: absolute; width: 131px; height: 30px; background: var(--button-blue);
    color: var(--white); font-family: inherit; font-size: 23px; line-height: 30px; text-align: center; border: 0;
  }
  .detail-label { position: absolute; left: 33px; font-size: 24px; line-height: 28px; }
</style>
</head>
<body>
<main class="canvas">
  <svg class="backdrop" width="1200" height="900" viewBox="0 0 1200 900" aria-hidden="true">
    <defs>
      <linearGradient id="stage-glow" x1="0" y1="0" x2="1" y2="1">
        <stop offset="0" stop-color="#0656a8"/>
        <stop offset="1" stop-color="#004c98"/>
      </linearGradient>
      <linearGradient id="floor-shade" x1="0" y1="0" x2="0" y2="1">
        <stop offset="0" stop-color="#0a2e58"/>
        <stop offset="1" stop-color="#061f3d"/>
      </linearGradient>
    </defs>
    <rect width="1200" height="900" fill="#00407f"/>
    <path d="M0 0 H1000 C1060 0 1085 70 1120 150 C1150 215 1185 250 1200 270 V900 H0 Z" fill="url(#stage-glow)"/>
    <path d="M1000 0 C1060 0 1085 70 1120 150 C1150 215 1185 250 1200 270" fill="none" stroke="#5a8fd0" stroke-width="3" opacity="0.6"/>
    <path d="M40 800 L1120 728 L1200 722 V900 H60 Z" fill="url(#floor-shade)"/>
    <path d="M440 790 L520 900 M780 765 L880 900" stroke="#1d4f8a" stroke-width="10" opacity="0.7"/>
  </svg>

  <h1 class="site-title">Pursevaultly.net</h1>

  <section class="panel panel--brand">
    <h2 class="panel-heading">Purse Vault</h2>
    <svg class="heading-icon" style="left:258px;top:6px" width="82" height="50" viewBox="0 0 82 50" aria-hidden="true">
      <g fill="none" stroke="#0152a0" stroke-width="3.5" stroke-linejoin="round">
        <path d="M2 4 H14 L22 32 H70 L78 8 H16"/>
        <path d="M20 16 H75 M22 24 H72 M32 8 V32 M44 8 V32 M56 8 V32 M66 8 V32"/>
        <path d="M22 32 L18 40 H72"/>
      </g>
      <circle cx="26" cy="45" r="4" fill="#0152a0"/><circle cx="66" cy="45" r="4" fill="#0152a0"/>
    </svg>
    <div class="preview-box" role="img" aria-label="Preview area for stored wallet documents"></div>

    <svg class="quick-icon" style="left:27px" width="66" height="52" viewBox="0 0 66 52" aria-hidden="true">
      <g fill="none" stroke="#fff" stroke-width="3"><rect x="2" y="10" width="62" height="34"/><path d="M2 10 L33 32 L64 10 M2 44 L26 27 M64 44 L40 27"/></g>
    </svg>
    <svg class="quick-icon" style="left:125px" width="54" height="52" viewBox="0 0 54 52" aria-hidden="true">
      <g fill="none" stroke="#fff" stroke-width="3"><circle cx="27" cy="26" r="23"/><ellipse cx="27" cy="26" rx="10" ry="23"/><path d="M4 26 H50 M8 14 H46 M8 38 H46 M27 3 V49"/></g>
    </svg>
    <svg class="quick-icon" style="left:202px" width="64" height="52" viewBox="0 0 64 52" aria-hidden="true">
      <g fill="none" stroke="#fff" stroke-width="3"><circle cx="22" cy="22" r="19"/><ellipse cx="22" cy="22" rx="8" ry="19"/><path d="M3 22 H41 M6 12 H38 M6 32 H38"/><circle cx="34" cy="32" r="10" fill="#f26a22"/><path d="M41 39 L58 50" stroke-width="5"/></g>
    </svg>
    <svg class="quick-icon" style="left:279px" width="36" height="52" viewBox="0 0 36 52" aria-hidden="true">
      <g fill="none" stroke="#fff" stroke-width="3"><ellipse cx="18" cy="26" rx="16" ry="20"/><path d="M18 15 V37 M7 26 H29" stroke-width="4"/></g>
    </svg>

    <span class="footer-link" style="left:12px">Contact</span>
    <span class="footer-link" style="left:140px">About Us</span>
    <span class="footer-link" style="left:279px">Store</span>
  </section>

  <section class="panel panel--login">
    <h2 class="panel-heading">Secure Login</h2>
    <svg class="heading-icon" style="left:224px;top:10px" width="91" height="40" viewBox="0 0 91 40" aria-hidden="true">
      <g fill="#0152a0">
        <path d="M2 20 L8 14 H50 V26 H44 L40 30 L36 26 L32 30 L28 26 L24 30 L20 26 H8 Z"/>
        <path d="M50 8 C56 0 62 0 66 2 L78 0 C88 4 90 14 88 20 C90 26 88 36 78 40 L66 38 C62 40 56 40 50 32 Z"/>
      </g>
      <circle cx="74" cy="20" r="5" fill="#f26a22"/>
    </svg>
    <label class="field-label" style="top:88px" for="username">Username</label>
    <input class="field-input" style="top:87px" id="username" type="text">
    <label class="field-label" style="top:143px" for="password">Password</label>
    <input class="field-input" style="top:142px" id="password" type="password">
    <label class="field-label" style="top:198px" for="question">Question</label>
    <input class="field-input" style="top:197px" id="question" type="text">
    <label class="field-label" style="top:256px" for="answers">Answers</label>
    <input class="field-input" style="top:254px" id="answers" type="text">
    <button class="action-button" style="left:85px;top:323px;height:31px" type="submit">Submit</button>
  </section>

  <section class="panel panel--home">
    <h2 class="panel-heading">Home Page</h2>
    <svg class="heading-icon" style="left:233px;top:6px" width="63" height="44" viewBox="0 0 63 44" aria-hidden="true">
      <g fill="none" stroke="#fff" stroke-width="3">
        <path d="M2 20 L31 3 L61 20 M7 18 V42 H56 V18 M18 9 V3 H24"/>
        <rect x="13" y="22" width="12" height="10"/><rect x="38" y="22" width="12" height="10"/><path d="M27 42 V30 H36 V42"/>
      </g>
    </svg>
    <span class="detail-label" style="top:86px">Name</span>
    <span class="detail-label" style="top:140px">Details</span>
    <button class="action-button" style="left:24px;top:195px" type="button">Back</button>
    <button class="action-button" style="left:179px;top:193px" type="button">Next</button>
    <button class="action-button" style="left:24px;top:278px" type="button">Edit</button>
    <button class="action-button" style="left:179px;top:275px" type="button">Delete</button>
  </section>
</main>
</body>
</html>
```